Surgical Procedure Room Letterhead

PLEASE DO NOT MAKE YOUR LETTERHEAD SIMILAR TO THE ONE I AM INCLUDING IN MY UPLOADS

Hello! I need my logo used to make a very clean, professional, simple letterhead that has all the pertinent information in it:
Location: 4182 NW 38th Lane, Suite 500
Tamarac, FL 33967
Phone: 954-218-4650
Fax: 800-642-9082

Can you please put this all on a word document that is easily editable? I will include my practice letterhead as an example ONLY of how easy it should be to write below the letterhead. Please don't make this letterhead the same as the one I am including in this example. They are two separate businesses.

Target Market(s)

Insurance companies

Industry/Entity Type

medical

Requirements
Must have
• classiness, elegance, simplicity
Should not have
• Please don't make your letterhead the same as the one that I included in my uploads

```html
<!DOCTYPE html>
<html lang="en">
<head>
<meta charset="utf-8">
<title>Clearview Suites Letterhead</title>
<link rel="stylesheet" href="https://fonts.googleapis.com/css2?family=Arimo:wght@400;700&family=Open+Sans:wght@400;600&display=swap">
<style>
  :root {
    --paper: #f6f3f3;
    --navy: #03305b;
    --gold: #d8b03c;
    --rule: #dcdada;
    --ink: #4a4a4a;
    --ink-soft: #5a5a5a;
    --white: #ffffff;
  }
  html, body {
    margin: 0;
    padding: 0;
    width: 942px;
    height: 1200px;
    overflow: hidden;
    background: var(--paper);
  }
  .letterhead {
    position: relative;
    width: 942px;
    height: 1200px;
    background: var(--paper);
    font-family: "Arimo", Arial, sans-serif;
    color: var(--ink);
    overflow: hidden;
  }
  .brand {
    position: absolute;
    left: 67px;
    top: 84px;
    display: flex;
    align-items: center;
    gap: 12px;
  }
  .brand-dot {
    width: 30px;
    height: 30px;
    border-radius: 50%;
    background: var(--gold);
  }
  .brand-name {
    font-family: "Arimo", Arial, sans-serif;
    font-weight: 700;
    font-size: 30px;
    letter-spacing: 0.5px;
    color: var(--navy);
  }
  .salutation {
    position: absolute;
    left: 65px;
    top: 297px;
    margin: 0;
    font-size: 25px;
    font-weight: 400;
    color: var(--ink-soft);
  }
  .letter-body {
    position: absolute;
    left: 65px;
    top: 362px;
    width: 815px;
    font-size: 14px;
    line-height: 20.3px;
    text-align: justify;
  }
  .letter-body p {
    margin: 0 0 20.5px;
  }
  .closing {
    position: absolute;
    left: 65px;
    top: 795px;
    margin: 0;
    font-size: 14px;
  }
  .signature {
    position: absolute;
    left: 67px;
    top: 875px;
    width: 125px;
    height: 46px;
    background: linear-gradient(90deg, rgba(30,38,60,0.08), rgba(30,38,60,0.18), rgba(30,38,60,0.06));
    border-radius: 4px;
  }
  .signer-name {
    position: absolute;
    left: 78px;
    top: 940px;
    margin: 0;
    font-size: 19px;
    color: var(--ink-soft);
  }
  .signer-title {
    position: absolute;
    left: 78px;
    top: 968px;
    margin: 0;
    font-size: 15px;
    color: var(--ink-soft);
  }
  .swoosh {
    position: absolute;
    left: 0;
    top: 0;
    width: 942px;
    height: 1200px;
  }
  .contact {
    position: absolute;
    right: 62px;
    top: 1062px;
    text-align: right;
    font-family: "Open Sans", Arial, sans-serif;
    font-size: 13.5px;
    line-height: 19px;
    color: var(--white);
  }
  .contact address {
    font-style: normal;
    margin-bottom: 9px;
  }
  .contact-line {
    display: flex;
    justify-content: flex-end;
    align-items: center;
    gap: 9px;
  }
  .contact-line svg {
    width: 13px;
    height: 13px;
    fill: var(--gold);
  }
</style>
</head>
<body>
<main class="letterhead">
  <div class="brand">
    <span class="brand-dot"></span>
    <span class="brand-name">Clearview Suites</span>
  </div>

  <h1 class="salutation">Dear Mr. Carter,</h1>

  <div class="letter-body">
    <p>Lorem ipsum dolor sit amet, consectetur adipiscing elit. Donec orci purus, luctus vitae dignissim eu, iaculis sed purus. Vivamus faucibus, ipsum nec aliquet viverra, leo mauris condimentum ligula, sit amet sagittis enim ligula quis arcu. Nam egestas tortor id nisi porttitor mattis. In tortor ante, ultricies in suscipit a, tempus non massa. Vivamus et auctor mi. Fusce vel massa nulla. Phasellus nec eros mauris, et scelerisque orci.</p>
    <p>Donec malesuada orci vitae nulla accumsan porta a id massa. Quisque accumsan iaculis magna sit amet fringilla. Maecenas consequat, magna eget tincidunt semper, odio nibh rutrum mi, id feugiat ante nisi eu risus. Vestibulum nunc orci, rhoncus a placerat in, ultricies in mi. Cras mattis varius eros, vel fringilla nisi suscipit eget. Quisque scelerisque sagittis nulla at porttitor.</p>
    <p>Sed id augue vitae urna euismod commodo aliquet a quam. Pellentesque arcu velit, cursus et malesuada ut, consequat et diam. Nullam erat sem, rhoncus id ullamcorper vitae, rhoncus et arcu. In ultricies ultricies nulla, ut rutrum nisi iaculis at. Donec eu magna a metus ornare faucibus. Fusce aliquet faucibus ultricies. Morbi semper, est id tincidunt gravida, sem arcu adipiscing lacus, ac bibendum nulla leo eu purus. Quisque nec diam sed risus consectetur a ccumsan quis quis nibh. Vestibulum id purus lorem.</p>
    <p>It is a long established fact that a reader will be distracted by the readable content of a page when looking at its layout. The point of using Lorem Ipsum is that it has a more-or-less normal distribution of letters, as opposed to using 'Content here, content here', making it look like readable English. Many desktop publishing packages</p>
  </div>

  <p class="closing">Sincerely,</p>
  <div class="signature" role="img" aria-label="Handwritten signature"></div>
  <p class="signer-name">Daniel Carter</p>
  <p class="signer-title">CEO/ Founder</p>

  <svg class="swoosh" viewBox="0 0 942 1200" aria-hidden="true">
    <path fill="var(--gold)" d="M0 1200 C 430 1130 830 1000 942 640 L 942 676 C 860 1000 560 1150 214 1200 Z"/>
    <path fill="var(--rule)" d="M150 1200 C 520 1148 850 1000 942 672 L 942 684 C 852 1004 560 1152 214 1200 Z"/>
    <path fill="var(--navy)" d="M214 1200 C 560 1150 852 1004 942 684 L 942 1200 Z"/>
  </svg>

  <div class="contact">
    <address>4182 NW 38th Lane<br>Suite 500<br>Tamarac, FL 33967</address>
    <div class="contact-line">
      <span>954-218-4650</span>
      <svg viewBox="0 0 24 24" aria-label="Phone" role="img"><path d="M6.6 10.8a15.2 15.2 0 0 0 6.6 6.6l2.2-2.2a1 1 0 0 1 1-.25 11.4 11.4 0 0 0 3.6.6 1 1 0 0 1 1 1V20a1 1 0 0 1-1 1A17 17 0 0 1 3 4a1 1 0 0 1 1-1h3.5a1 1 0 0 1 1 1c0 1.25.2 2.45.6 3.6a1 1 0 0 1-.25 1z"/></svg>
    </div>
    <div class="contact-line">
      <span>800-642-9082</span>
      <svg viewBox="0 0 24 24" aria-label="Fax" role="img"><path d="M7 2h10v5H7zM4 8h16a2 2 0 0 1 2 2v8h-4v-4H6v4H2v-8a2 2 0 0 1 2-2zm4 8h8v6H8z"/></svg>
    </div>
  </div>
</main>
</body>
</html>
```